Mental health agency needs an ad for brochure

Please provide us with a half page (W 8.5 inches x H 5.5 inches) advertising our company. We are a mental health agency that provides training, education, and consultation for companies that serve children, adolescents, or adults. We can offer training and education to help companies better serve their clientele and consultation about how companies are currently working with their staff or clientele. Our website is www.quellbrook.com and they can contact us at info@haverstoneinstitute.com or 503-847-2163.

```html
<!DOCTYPE html>
<html lang="en">
<head>
<meta charset="utf-8">
<title>The Haverstone Institute Northwest – Brochure Ad</title>
<link rel="stylesheet" href="https://fonts.googleapis.com/css2?family=Alegreya+Sans:wght@400;700;800&family=Montserrat:wght@600;700&family=Tinos:wght@700&display=swap">
<style>
  :root {
    --navy: #0b2d5c;
    --headline: #10296a;
    --teal: #0a8bb5;
    --grey: #767676;
    --paper-light: #fbfbfb;
    --paper-dark: #e4e4e4;
    --petal: #d9536d;
    --petal-soft: #f1c3cc;
    --ink: #111111;
    --white: #ffffff;
  }
  * { margin: 0; padding: 0; box-sizing: border-box; }
  html, body { width: 1200px; height: 776px; overflow: hidden; background: var(--white); }
  .ad {
    position: relative;
    width: 1200px;
    height: 776px;
    overflow: hidden;
    background: linear-gradient(100deg, var(--paper-dark) 0%, var(--paper-light) 45%, #f2f2f2 70%, var(--paper-dark) 100%);
    font-family: "Alegreya Sans", sans-serif;
  }
  .petal-heart {
    position: absolute;
    left: 560px;
    top: 150px;
    width: 620px;
    height: 560px;
    background: radial-gradient(ellipse 50% 48% at 50% 50%, var(--petal) 0%, #e27a8e 45%, var(--petal-soft) 75%, rgba(241,195,204,0) 100%);
  }
  .brand {
    position: absolute;
    left: 40px;
    top: 150px;
    width: 300px;
    text-align: center;
    color: var(--navy);
    font-weight: 700;
    font-size: 24px;
    line-height: 28px;
  }
  .brand-dot {
    display: block;
    width: 96px;
    height: 96px;
    margin: -110px auto 16px;
    border-radius: 50%;
    background: var(--navy);
  }
  .headline {
    position: absolute;
    left: 405px;
    top: 44px;
    width: 770px;
    text-align: center;
    color: var(--headline);
    font-weight: 800;
    font-size: 64px;
    line-height: 60px;
    letter-spacing: -0.5px;
  }
  .section-title {
    position: absolute;
    left: 600px;
    top: 256px;
    width: 490px;
    text-align: center;
    color: var(--white);
    font-family: "Tinos", serif;
    font-weight: 700;
    font-size: 46px;
    letter-spacing: -1px;
  }
  .service {
    position: absolute;
    top: 403px;
    height: 234px;
    color: var(--white);
    font-size: 23.5px;
    line-height: 28.2px;
    text-align: center;
    padding-top: 48px;
  }
  .service strong { font-weight: 700; }
  .service::before {
    content: "";
    position: absolute;
    top: -87px;
    left: var(--dome-x);
    width: 174px;
    height: 174px;
    margin-left: -87px;
    border-radius: 50%;
    background: inherit;
    z-index: -1;
  }
  .service-training { left: 0; width: 412px; background: var(--navy); --dome-x: 197px; padding-left: 18px; padding-right: 18px; }
  .service-therapy { left: 412px; width: 376px; background: var(--teal); --dome-x: 188px; padding-left: 14px; padding-right: 14px; }
  .service-consult { left: 788px; width: 412px; background: var(--grey); --dome-x: 222px; padding-left: 18px; padding-right: 14px; }
  .services { position: absolute; inset: 0; isolation: isolate; }
  .service-icon { position: absolute; z-index: 2; }
  .contact {
    position: absolute;
    left: 31px;
    top: 668px;
    font-family: "Montserrat", sans-serif;
  }
  .contact-title { color: var(--ink); font-weight: 700; font-size: 26px; line-height: 30px; letter-spacing: 0.5px; }
  .contact-line {
    display: flex;
    align-items: center;
    gap: 10px;
    color: var(--teal);
    font-weight: 600;
    font-size: 21.5px;
    line-height: 27px;
  }
  .contact-line svg { flex: none; }
  .website {
    position: absolute;
    right: 30px;
    top: 710px;
    color: var(--teal);
    font-family: "Montserrat", sans-serif;
    font-weight: 700;
    font-size: 40px;
    letter-spacing: 0.5px;
  }
</style>
</head>
<body>
<main class="ad">
  <div class="petal-heart" role="img" aria-label="Photograph of red rose petals arranged in a heart shape"></div>

  <div class="brand">
    <span class="brand-dot"></span>
    The Haverstone Institute<br>Northwest, LLC
  </div>

  <h1 class="headline">Nurture Authentic and Safe<br>Relationships Around You</h1>

  <h2 class="section-title">WHAT WE PROVIDE</h2>

  <section class="services">
    <div class="service service-training">
      Reduce stress and develop poise in managing behaviors <strong>in your school</strong> and <strong>non-profit child-serving organizations</strong> with training in the area of trauma and its effect on the brain and body.
    </div>
    <div class="service service-therapy">
      Develop confidence and become self-assured to build strong and reliable boundaries in relationship with others using body-oriented therapy, offered for <strong>individuals, couples, and families.</strong>
    </div>
    <div class="service service-consult">
      Decrease staff stress, burnout, and absenteeism while increasing staff authenticity and openness using feedback and heatmapping tools <strong>across teams</strong> and <strong>departments in your organization.</strong>
    </div>

    <svg class="service-icon" style="left:130px;top:340px" width="132" height="96" viewBox="0 0 132 96" aria-hidden="true">
      <path d="M0 28 C10 24 30 26 42 34 C40 60 50 80 66 94 C30 96 6 72 0 28Z" fill="#fff"/>
      <path d="M132 28 C122 24 102 26 90 34 C92 60 82 80 66 94 C102 96 126 72 132 28Z" fill="#fff"/>
      <path d="M66 2 C48 22 38 50 42 72 C46 86 56 94 66 94 C76 94 86 86 90 72 C94 50 84 22 66 2Z" fill="#fff"/>
      <circle cx="66" cy="42" r="7" fill="none" stroke="var(--navy)" stroke-width="2.5"/>
      <path d="M56 78 C56 62 58 52 66 52 C74 52 76 62 76 78 M50 86 C56 78 76 78 82 86" fill="none" stroke="var(--navy)" stroke-width="2.5" stroke-linecap="round"/>
    </svg>

    <svg class="service-icon" style="left:549px;top:340px" width="102" height="102" viewBox="0 0 102 102" aria-hidden="true">
      <g fill="#fff">
        <rect x="0" y="0" width="18" height="18" rx="3"/>
        <rect x="84" y="0" width="18" height="18" rx="3"/>
        <rect x="0" y="84" width="18" height="18" rx="3"/>
        <rect x="84" y="84" width="18" height="18" rx="3"/>
        <rect x="26" y="6" width="50" height="6" rx="3"/>
        <rect x="26" y="90" width="50" height="6" rx="3"/>
        <rect x="6" y="26" width="6" height="50" rx="3"/>
        <rect x="90" y="26" width="6" height="50" rx="3"/>
        <circle cx="51" cy="42" r="11"/>
        <path d="M34 70 C34 56 42 52 51 52 C60 52 68 56 68 70Z"/>
      </g>
    </svg>

    <svg class="service-icon" style="left:960px;top:344px" width="102" height="94" viewBox="0 0 102 94" aria-hidden="true">
      <path d="M42 6 H96 A6 6 0 0 1 102 12 V38 A6 6 0 0 1 96 44 H60 L48 56 L50 44 H46" fill="none" stroke="#fff" stroke-width="5" stroke-linejoin="round"/>
      <g fill="#fff">
        <circle cx="62" cy="25" r="4"/><circle cx="74" cy="25" r="4"/><circle cx="86" cy="25" r="4"/>
        <circle cx="30" cy="34" r="17"/>
        <path d="M0 92 C0 66 12 56 30 56 C48 56 60 66 60 92 C44 96 14 96 0 92Z"/>
      </g>
      <path d="M20 58 L30 72 L40 58" fill="none" stroke="var(--grey)" stroke-width="3"/>
    </svg>
  </section>

  <address class="contact" style="font-style:normal">
    <p class="contact-title">CONTACT US AT</p>
    <p class="contact-line">
      <svg width="22" height="22" viewBox="0 0 22 22" aria-hidden="true" fill="none" stroke="#8a8a8a" stroke-width="1.6">
        <circle cx="11" cy="11" r="9.5"/><ellipse cx="11" cy="11" rx="4.5" ry="9.5"/><path d="M1.5 11 H20.5 M3 6 H19 M3 16 H19"/>
      </svg>
      info@haverstoneinstitute.com
    </p>
    <p class="contact-line">
      <svg width="22" height="18" viewBox="0 0 22 18" aria-hidden="true">
        <rect x="0" y="1" width="22" height="16" rx="1.5" fill="#8a8a8a"/><path d="M0 2 L11 10 L22 2" fill="none" stroke="#f4f4f4" stroke-width="1.6"/>
      </svg>
      503-847-2163
    </p>
  </address>

  <p class="website">www.quellbrook.com</p>
</main>
</body>
</html>
```